maintenace book service online with time table

i would like to do a service book to keep his try for each machine and show it status ( install , jacking up , demolition , breakdown and repair , check up , inspection ) and description of each work by type and attached the scan file and if have any cost or reference , show it in each record

```html
<!DOCTYPE html>
<html lang="en">
<head>
<meta charset="UTF-8">
<title>Service History Book</title>
<link rel="stylesheet" href="https://fonts.googleapis.com/css2?family=Patrick+Hand&family=Roboto:wght@400;500&display=swap">
<style>
  :root {
    --page-bg: #e4dcc6;
    --card-bg: #ffffff;
    --accent: #f5dc9c;
    --ink: #212121;
    --muted: #a3a3a3;
    --hint: #757575;
    --line: #e0e0e0;
    --required: #d93025;
    --banner-light: #e9dfb4;
    --banner-mid: #b59a72;
    --banner-dark: #5a3a2c;
  }
  * { box-sizing: border-box; margin: 0; padding: 0; }
  html, body {
    width: 1200px;
    height: 647px;
    overflow: hidden;
    background: var(--page-bg);
    font-family: "Roboto", Arial, sans-serif;
    color: var(--ink);
  }
  .canvas { position: relative; width: 1200px; height: 647px; overflow: hidden; }

  .banner {
    position: absolute; left: 0; top: 0; width: 1200px; height: 263px;
    background:
      radial-gradient(ellipse 160px 130px at 600px 70px, var(--banner-dark) 0%, rgba(90,58,44,0.6) 45%, rgba(181,154,114,0) 100%),
      linear-gradient(100deg, #d8cfa0 0%, var(--banner-light) 30%, var(--banner-mid) 50%, var(--banner-light) 70%, #cbbd8e 100%);
  }

  .edit-button {
    position: absolute; left: 1117px; top: 17px; width: 52px; height: 42px;
    background: var(--accent); border-radius: 2px;
    display: flex; align-items: center; justify-content: center;
  }

  .form-card {
    position: absolute; left: 293px; top: 169px; width: 599px; height: 520px;
    background: var(--card-bg);
    border-top: 8px solid var(--accent);
    border-radius: 3px 3px 0 0;
    box-shadow: 0 1px 3px rgba(0,0,0,0.15);
  }

  .form-title {
    position: absolute; left: 31px; top: 36px;
    font-family: "Patrick Hand", "Comic Sans MS", cursive;
    font-size: 34px; font-weight: 400; color: var(--ink);
  }
  .required-note {
    position: absolute; left: 31px; top: 142px;
    font-size: 13px; color: var(--required);
  }

  .question { position: absolute; left: 31px; }
  .question-label {
    font-family: "Patrick Hand", "Comic Sans MS", cursive;
    font-size: 19px; color: var(--ink);
  }
  .question-label .star { color: var(--required); }
  .field-caption { font-size: 11px; color: var(--hint); margin-top: 6px; }
  .text-field {
    margin-top: 14px; width: 264px; padding-bottom: 6px;
    border-bottom: 1px solid var(--line);
    font-size: 15px; color: var(--muted);
  }
  .date-field {
    margin-top: 6px; width: 113px; padding-bottom: 6px;
    border-bottom: 1px solid var(--line);
    font-size: 16px; color: var(--ink);
  }
  .q-machine { top: 194px; }
  .q-install { top: 311px; }
  .q-jackup { top: 440px; }

  .feedback-icon { position: absolute; left: 13px; top: 611px; }
</style>
</head>
<body>
  <div class="canvas">
    <div class="banner" role="img" aria-label="Header photo of an open book with two pages curled into a heart, warm sepia tones"></div>

    <div class="edit-button" aria-label="Edit">
      <svg width="22" height="22" viewBox="0 0 24 24"><path fill="#212121" d="M3 17.25V21h3.75L17.8 9.94l-3.75-3.75L3 17.25zM20.7 7.04a1 1 0 0 0 0-1.41l-2.34-2.34a1 1 0 0 0-1.41 0l-1.83 1.83 3.75 3.75 1.83-1.83z"/></svg>
    </div>

    <main class="form-card">
      <h1 class="form-title">Service History Book</h1>
      <p class="required-note">* Required</p>

      <div class="question q-machine">
        <div class="question-label">Machine ID <span class="star">*</span></div>
        <div class="text-field">Your answer</div>
      </div>

      <div class="question q-install">
        <div class="question-label">Install Date <span class="star">*</span></div>
        <div class="field-caption">Date</div>
        <div class="date-field">mm/dd/yyyy</div>
      </div>

      <div class="question q-jackup">
        <div class="question-label">Jack Up Date <span class="star">*</span></div>
      </div>
    </main>

    <svg class="feedback-icon" width="20" height="20" viewBox="0 0 20 20" aria-label="Feedback">
      <path d="M3 2h14a1 1 0 0 1 1 1v10a1 1 0 0 1-1 1H6l-4 4V3a1 1 0 0 1 1-1z" fill="#5f5f5f"/>
      <rect x="9.2" y="4.5" width="1.6" height="5" fill="#e4dcc6"/>
      <rect x="9.2" y="10.8" width="1.6" height="1.6" fill="#e4dcc6"/>
    </svg>
  </div>
</body>
</html>
```